Stated Income Loans

Flyer design to be used on social media platforms (i.e. Chatterly, Snapfeed etc.)

Target Market(s)

Real Estate Investors

Requirements
Must have
• INVESTOR STATED INCOME LOANS
• "IT'S TIME TO THINK BIG"
• * Purchase or Refinance up to 3 Million
• * No Income Docs or Bank Statements
• * Vacant Properties Allowed
• * Minimum Credit Score 620
• * Cash Out up to 80%
• Same Day Pre-Approval
• 20-30 Day Close
• Call Marcus Delby today...
• Bluecrest Lending Group, Inc.
• Phone (800) 947-2651 x 17
• Direct (240) 368-9042
• www.bluecrestlendgrp.example
• NMLS #738164 / #50817
Should not have
• Do not use same color scheme as website. Be creative.

```html
<!DOCTYPE html>
<html lang="en">
<head>
<meta charset="utf-8">
<title>Investor Stated Income Loans</title>
<link href="https://fonts.googleapis.com/css2?family=Jost:wght@300;400;500;700&display=swap" rel="stylesheet">
<style>
  :root {
    --green: #4e6812;
    --green-glass: rgba(78, 104, 18, 0.8);
    --paper: #f0f0ee;
    --white: #ffffff;
    --ink: #1d1d1d;
    --photo-light: #a9a9a9;
    --photo-dark: #222222;
  }
  * { box-sizing: border-box; margin: 0; padding: 0; }
  html, body { width: 957px; height: 1200px; overflow: hidden; background: var(--paper); }
  body { font-family: "Jost", "Futura", sans-serif; color: var(--ink); }
  .flyer { position: relative; width: 957px; height: 1200px; background: var(--paper); overflow: hidden; }

  .masthead {
    position: absolute; top: 0; left: 0; width: 100%; height: 112px;
    background: var(--green); display: flex; align-items: center; justify-content: center;
  }
  .masthead h1 { color: var(--white); font-weight: 700; font-size: 44px; letter-spacing: 1px; white-space: nowrap; }

  .hero-photo {
    position: absolute; top: 112px; left: 0; width: 100%; height: 440px;
    background: linear-gradient(180deg, var(--photo-dark) 0%, var(--photo-light) 30%, #7c7c7c 60%, var(--photo-dark) 100%);
  }
  .hero-curve { position: absolute; top: 490px; left: 0; width: 957px; height: 64px; }

  .slogan-panel {
    position: absolute; top: 250px; left: 0; width: 440px; height: 250px;
    background: var(--green-glass); padding: 14px 0 0 56px; color: var(--white); white-space: nowrap;
  }
  .slogan-panel .line-light { display: block; font-weight: 300; font-size: 56px; line-height: 62px; }
  .slogan-panel .line-bold { display: block; font-weight: 700; font-size: 66px; line-height: 80px; }

  .features { position: absolute; top: 568px; left: 0; width: 100%; }
  .feature-row { display: flex; justify-content: center; gap: 40px; }
  .feature-row.second { margin-top: 34px; gap: 60px; }
  .feature { width: 180px; text-align: center; }
  .feature svg { width: 78px; height: 78px; display: block; margin: 0 auto 12px; }
  .feature p { font-size: 18px; line-height: 21px; color: var(--ink); }

  .contact { position: absolute; top: 900px; left: 0; width: 100%; height: 195px; }
  .band-left { position: absolute; left: 0; top: 50px; width: 60px; height: 80px; background: var(--green); }
  .brand-card {
    position: absolute; left: 36px; top: 0; width: 300px; height: 180px; background: var(--white);
    box-shadow: 0 6px 14px rgba(0,0,0,0.25); display: flex; align-items: center; gap: 12px; padding: 0 22px;
  }
  .brand-dot { width: 34px; height: 34px; border-radius: 50%; background: var(--green); flex: none; }
  .brand-name { font-size: 22px; font-weight: 500; color: var(--green); line-height: 27px; }

  .call-line { position: absolute; left: 360px; top: 42px; font-size: 22px; color: var(--ink); white-space: nowrap; }
  .call-line strong { color: var(--green); font-weight: 700; }
  .band-right {
    position: absolute; left: 346px; top: 82px; width: 611px; height: 108px; background: var(--green);
    padding: 8px 0 0 20px; color: var(--white); font-size: 18px; line-height: 23px; white-space: nowrap;
  }
  .agent-photo {
    position: absolute; right: 40px; top: 22px; width: 200px; height: 168px;
    background: linear-gradient(180deg, #7d6a5a 0%, #3a3430 45%, #141414 100%);
  }

  .social { position: absolute; top: 1112px; left: 0; width: 100%; display: flex; justify-content: center; gap: 24px; }
  .social-item { display: flex; align-items: center; gap: 6px; font-size: 14px; color: var(--green); }
  .social-item .ring { width: 22px; height: 22px; border: 2px solid var(--green); border-radius: 50%; }

  .footer-rule { position: absolute; top: 1160px; left: 0; width: 100%; height: 8px; background: var(--green); }
</style>
</head>
<body>
<main class="flyer">
  <header class="masthead"><h1>INVESTOR STATED INCOME LOANS</h1></header>

  <div class="hero-photo" role="img" aria-label="Black and white photo of three business people silhouetted against tall windows overlooking a city skyline"></div>
  <svg class="hero-curve" viewBox="0 0 957 64" preserveAspectRatio="none" aria-hidden="true">
    <path d="M0 10 Q 480 0 957 54 L957 64 L0 64 Z" fill="#f0f0ee"/>
  </svg>

  <div class="slogan-panel">
    <span class="line-light">It’s</span>
    <span class="line-light">TIME To</span>
    <span class="line-bold">THINK BIG</span>
  </div>

  <section class="features">
    <div class="feature-row">
      <div class="feature">
        <svg viewBox="0 0 64 64" fill="none" stroke="#4e6812" stroke-width="2.5" stroke-linecap="round" stroke-linejoin="round">
          <circle cx="32" cy="32" r="13"/>
          <path d="M36 26h-6a3 3 0 0 0 0 6h4a3 3 0 0 1 0 6h-7M32 22v4M32 38v4"/>
          <path d="M12 28a20 20 0 0 1 34-12l-2-6M52 36a20 20 0 0 1-34 12l2 6"/>
        </svg>
        <p>Purchase or Refinance up to 3 Million</p>
      </div>
      <div class="feature">
        <svg viewBox="0 0 64 64" fill="none" stroke="#4e6812" stroke-width="2.5" stroke-linejoin="round" stroke-linecap="round">
          <path d="M16 6h28l6 6v46H16z"/>
          <path d="M36 16h-6a3 3 0 0 0 0 6h4a3 3 0 0 1 0 6h-7M32 12v4M32 28v4"/>
          <path d="M22 40h22M22 46h22M22 52h14"/>
        </svg>
        <p>No Income Docs or Bank Statements</p>
      </div>
      <div class="feature">
        <svg viewBox="0 0 64 64" fill="none" stroke="#4e6812" stroke-width="2.5" stroke-linejoin="round">
          <path d="M8 26L32 8l24 18"/>
          <path d="M12 24v32h40V24"/>
          <rect x="18" y="30" width="8" height="8"/><rect x="38" y="30" width="8" height="8"/>
          <path d="M28 56V42h8v14M6 56h52"/>
        </svg>
        <p>Vacant Properties Allowed</p>
      </div>
      <div class="feature">
        <svg viewBox="0 0 64 64" fill="none" stroke="#4e6812" stroke-width="2.5" stroke-linejoin="round" stroke-linecap="round">
          <rect x="8" y="18" width="48" height="30" rx="4" transform="rotate(-30 32 33)"/>
          <path d="M14 36l36-20M22 44l8-4M40 34l6-3"/>
          <path d="M20 58h28"/>
        </svg>
        <p>Minimum Credit<br>Score 620</p>
      </div>
    </div>
    <div class="feature-row second">
      <div class="feature">
        <svg viewBox="0 0 64 64" fill="none" stroke="#4e6812" stroke-width="2.5" stroke-linejoin="round">
          <rect x="6" y="22" width="36" height="22" rx="2"/>
          <circle cx="24" cy="33" r="6"/>
          <path d="M10 18l30-6 4 10"/>
          <ellipse cx="50" cy="34" rx="9" ry="3"/>
          <path d="M41 34v16c0 2 4 3 9 3s9-1 9-3V34M41 40c0 2 4 3 9 3s9-1 9-3M41 46c0 2 4 3 9 3s9-1 9-3"/>
        </svg>
        <p>Cash Out up to 80%</p>
      </div>
      <div class="feature">
        <svg viewBox="0 0 64 64" fill="none" stroke="#4e6812" stroke-width="2.5" stroke-linejoin="round" stroke-linecap="round">
          <rect x="6" y="8" width="44" height="40" rx="2"/>
          <path d="M6 16h44M12 12h2M18 12h2"/>
          <path d="M14 30l6 6 12-12"/>
          <path d="M56 22l4 4-18 22-6 2 2-6z"/>
        </svg>
        <p>Same Day Pre-Approval</p>
      </div>
      <div class="feature">
        <svg viewBox="0 0 64 64" fill="none" stroke="#4e6812" stroke-width="2.5" stroke-linejoin="round" stroke-linecap="round">
          <rect x="6" y="10" width="44" height="40" rx="3"/>
          <path d="M6 20h44M16 6v8M28 6v8M40 6v8"/>
          <path d="M18 34l6 6 10-10"/>
          <circle cx="48" cy="48" r="10" fill="#f0f0ee"/>
          <path d="M48 43v5l3 3"/>
        </svg>
        <p>20-30 Day Close</p>
      </div>
    </div>
  </section>

  <section class="contact">
    <div class="band-left"></div>
    <div class="brand-card">
      <span class="brand-dot"></span>
      <span class="brand-name">Bluecrest Lending Group, Inc.</span>
    </div>
    <p class="call-line">Call <strong>Marcus Delby</strong> today...</p>
    <div class="band-right">
      <p>Phone: (800) 947-2651 x 17</p>
      <p>Direct: (240) 368-9042</p>
      <p>www.bluecrestlendgrp.example</p>
      <p>NMLS #738164 / #50817</p>
    </div>
    <div class="agent-photo" role="img" aria-label="Portrait of the loan officer in a dark suit and tie"></div>
  </section>

  <nav class="social">
    <span class="social-item"><span class="ring"></span>Chatterly</span>
    <span class="social-item"><span class="ring"></span>Chirpline</span>
    <span class="social-item"><span class="ring"></span>Workgrid</span>
  </nav>

  <div class="footer-rule"></div>
</main>
</body>
</html>
```